Bauzaunplane für Weihnachtsmarkt
Zielgruppe
Endverbraucher, die den Weihnachtsmarkt besuchen / besuchen sollen.
Aufgabenstellung
Benötigt wird ein Entwurf für eine Bauzaunplane (B) 2,12m x (H) 1,72m. Diese wird auf einem Weihnachtsmarkt als Sichtblende eingesetzt.
Die Gestaltung soll Atmosphäre vermitteln und ggf. Bezug zu Nikolaus, Engeln und anderen Adventssysmbolen nehmen (Hinweis: Der Weihnachtsmann kommt ind er Bibel nicht vor!)
Der Claim" Wir wünschen Ihnen eine schöne Zeit auf dem Quendlitzer Weihnachtsmarkt" soll in das Motiv integriert werden.
Das Banner wird anschließend im Digitaldruck 4/0 C produziert. gefordert ist abschließend eine druckfähige Vorlage mit ausreichender Auflösung (ca. 100dpi auf das Endformat) vorzugsweise PDF/X3 - ISOcoatedV2ECI.

```html
<!DOCTYPE html>
<html lang="de">
<head>
<meta charset="utf-8">
<title>Bauzaunplane – Quendlitzer Weihnachtsmarkt</title>
<link rel="stylesheet" href="https://fonts.googleapis.com/css2?family=Pinyon+Script&family=Almendra+SC&display=swap">
<style>
  :root {
    --page-bg: #f2f2f2;
    --ribbon: #c6902f;
    --ribbon-edge: #b07d22;
    --text-light: #fffaf0;
    --photo-navy: #1f2a4a;
    --photo-red: #b3261e;
    --photo-pink: #d85a8a;
    --photo-cream: #efe6d8;
    --photo-amber: #e9a54a;
    --photo-glow: #f8e3a0;
    --photo-deep: #5a1c12;
  }
  html, body {
    margin: 0;
    padding: 0;
    width: 1200px;
    height: 772px;
    overflow: hidden;
    background: var(--page-bg);
  }
  .banner {
    position: absolute;
    left: 112px;
    top: 16px;
    width: 976px;
    height: 740px;
    overflow: hidden;
  }
  .banner__photo {
    position: absolute;
    inset: 0;
    background:
      radial-gradient(ellipse 22% 16% at 41% 25%, var(--photo-pink) 0%, transparent 100%),
      radial-gradient(ellipse 24% 30% at 46% 70%, var(--photo-cream) 0%, transparent 100%),
      radial-gradient(ellipse 26% 48% at 12% 72%, var(--photo-navy) 0%, transparent 100%),
      radial-gradient(ellipse 10% 40% at 25% 60%, var(--photo-red) 0%, transparent 100%),
      radial-gradient(ellipse 40% 55% at 80% 40%, var(--photo-glow) 0%, var(--photo-amber) 45%, transparent 100%),
      linear-gradient(170deg, var(--photo-red) 0%, var(--photo-deep) 45%, #8a3a1c 100%);
  }
  .banner__ribbon {
    position: absolute;
    left: 0;
    top: 574px;
    width: 937px;
    height: 137px;
  }
  .claim {
    position: absolute;
    left: 0;
    top: 574px;
    width: 900px;
    height: 137px;
    margin: 0;
    color: var(--text-light);
  }
  .claim__intro {
    position: absolute;
    left: 74px;
    top: 14px;
    margin: 0;
    font-family: "Pinyon Script", cursive;
    font-size: 33px;
    line-height: 1;
    white-space: nowrap;
  }
  .claim__market {
    position: absolute;
    left: 16px;
    top: 62px;
    width: 832px;
    margin: 0;
    font-family: "Almendra SC", serif;
    font-weight: 400;
    font-size: 46px;
    letter-spacing: 5px;
    word-spacing: 22px;
    line-height: 1;
    text-align: center;
    white-space: nowrap;
  }
</style>
</head>
<body>
  <main class="banner">
    <div class="banner__photo" role="img" aria-label="Foto: lächelndes Paar in Winterkleidung mit Glühweintassen vor einem beleuchteten Weihnachtsmarktstand mit Lebkuchenherzen und Nüssen"></div>

    <svg class="banner__ribbon" viewBox="0 0 937 137" aria-hidden="true">
      <polygon points="0,0 937,0 905,68.5 937,137 0,137" fill="var(--ribbon)"/>
      <polyline points="937,0 905,68.5 937,137" fill="none" stroke="var(--ribbon-edge)" stroke-width="2"/>
    </svg>

    <header class="claim">
      <p class="claim__intro">Wir wünschen Ihnen eine schöne Zeit auf dem</p>
      <h1 class="claim__market">Quendlitzer Weihnachtsmarkt</h1>
    </header>
  </main>
</body>
</html>
```